We have a small 501C Non-Profit, called Youngsters Unite. The non-profit was started by my son and his friends during the Gulf Oil Spill. We would like to update the website that currently sits on Domivault.com. I'm not sure how we transfer over the domain or get them to host it with your new design. I've attached a link of the old site that we developed. We are open to any ideas regarding hosting.

We would basically like a look that is youth (teen, college age) oriented that will drive teens and donors to the site. Our goal is to get onto Plixa Drives, get grants and make major donations with little to no administration expense. We will get sponsors to pay for the administration costs. So we will be looking for sponsors to support the overhead and 100% of donor money will go to causes important to teens.

http://www.youngstersunite.org

Target Market(s)

Teenagers and Individual Sponsors. Adults that want to help teens with an important cause.

Industry/Entity Type

Non-Profit

Requirements
Must have
• We are very open to ideas. It would be good to have a:

Home-with Mission Statement and Photos or Graphics
Donate-100% of Donations Go To Causes (with Coinvo Link)
Become A Sponsor-Insert Contact Information In This Section.
How It All Got Started -with info, articles, events, video, etc. from Gulf Oil Spill, Our Founder photo.
Contact-Change phone number to 555-804-2739. Keep e-mail and mailing the same.

You can use some existing photos from current site if you would like. All the Recent Event Photos, Founder Photo, 3 people holding check photo were all taken by me so there are no rights issues with those.

YU Mission Statement:

To demonstrate to the world that Youngsters Unite about the environment, each other and world peace through fund raising and other philanthropic efforts.
Nice to have
• Youngsters Unite Logo If Possible

Photo of 3 people, holding check, from existing home page in new History Section.

Kindpaw League Story and Logo in History Section

WRX Video in History Section

Helpio4
http://www.helpio4.net/stories/youth-launches-charity-to-fund-relief-for-wildlife-harmed-by-coastal-slick.html
Should not have
• Delete Blog Section
Delete Founder Section
Delete Recent Events
Delete How To Get Involved

```html
<!DOCTYPE html>
<html lang="en">
<head>
<meta charset="utf-8">
<title>Youngsters Unite</title>
<link rel="stylesheet" href="https://fonts.googleapis.com/css2?family=Marcellus&family=Fjalla+One&family=Roboto+Condensed:wght@700&family=Gelasio&display=swap">
<style>
:root{
  --sky-top:#9fd3ec;
  --sky-bottom:#e3f2f8;
  --page:#e8ebed;
  --teal:#12b5c5;
  --teal-dark:#0a7fb4;
  --navy:#1c3f7e;
  --blue-title:#1a7fd4;
  --orange:#f39a1e;
  --orange-dark:#e8891a;
  --green:#8cc21e;
  --green-dark:#78a814;
  --ink:#222;
  --white:#fff;
  --footer:#3a3a3a;
  --photo-warm:#8a7358;
  --photo-field:#6f8a5a;
  --photo-crowd:#a49a8a;
}
*{box-sizing:border-box;margin:0;padding:0}
html,body{width:765px;height:1200px;overflow:hidden}
body{position:relative;background:var(--page);font-family:Arial,Helvetica,sans-serif;color:var(--ink)}
.abs{position:absolute}
.header{left:0;top:0;width:765px;height:200px;background:linear-gradient(180deg,var(--sky-top),var(--sky-bottom))}
.brand{left:30px;top:56px;display:flex;align-items:center;gap:8px}
.brand-name{font-family:'Marcellus',serif;font-size:31px;color:#111}
.brand-dot{width:50px;height:50px;border-radius:50%;background:var(--navy)}
.social-badge{left:572px;top:62px;width:148px;height:37px;border-radius:5px;background:linear-gradient(180deg,#3b64b0,var(--navy));color:var(--white);font-size:13px;font-weight:bold;display:flex;align-items:center;justify-content:center;letter-spacing:.5px}
.nav{left:14px;top:155px;width:738px;height:40px;border-radius:14px;background:linear-gradient(180deg,#27d3c8,var(--teal) 45%,var(--teal-dark));display:flex;justify-content:space-around;align-items:center;box-shadow:0 2px 4px rgba(0,0,0,.25)}
.nav a{color:var(--white);text-decoration:none;font-size:11px;text-transform:uppercase}
.slider{left:36px;top:210px;width:692px;height:320px;background:var(--white);padding:4px;border-radius:0 0 50% 50%/0 0 22px 22px;box-shadow:0 1px 4px rgba(0,0,0,.3)}
.slide-photo{width:100%;height:100%;border-radius:0 0 50% 50%/0 0 20px 20px;background:linear-gradient(120deg,#d6d0c2,var(--photo-warm) 40%,#5a4a3c);position:relative;overflow:hidden}
.slide-caption{position:absolute;left:0;right:0;bottom:0;height:40px;background:rgba(0,0,0,.55);color:var(--white);font-family:'Gelasio',serif;font-size:22px;text-align:center;line-height:38px}
.arrow{top:333px;width:33px;height:37px;border-radius:4px;background:linear-gradient(180deg,#3fb4ea,#0c79c1)}
.arrow-left{left:27px}.arrow-right{left:705px}
.mission-title{left:35px;top:553px;font-family:'Gelasio',serif;font-size:24px;color:var(--blue-title)}
.mission-text{left:37px;top:595px;width:410px;font-size:13.5px;line-height:19px}
.read-more{font-size:10px;color:var(--blue-title);text-decoration:underline}
.mission-more{left:38px;top:638px}
.mission-photo{left:465px;top:568px;width:263px;height:102px;background:var(--white);padding:4px;box-shadow:0 1px 3px rgba(0,0,0,.3)}
.mission-photo div{width:100%;height:100%;background:linear-gradient(180deg,#d9d3c6 0%,#cfc8b8 40%,var(--photo-field) 55%,#4f6b3c)}
.causes{left:28px;top:696px;width:710px;display:flex;justify-content:space-between}
.cause{display:flex;align-items:center;gap:6px;font-family:'Fjalla One',sans-serif;font-size:21px;color:var(--orange)}
.cause svg{width:19px;height:19px}
.card{background:var(--white);padding:4px;box-shadow:0 1px 4px rgba(0,0,0,.3)}
.donate{left:29px;top:757px;width:163px;height:168px;border-radius:0 0 50% 50%/0 0 22px 22px}
.donate-inner{height:100%;background:var(--green);border-radius:0 0 50% 50%/0 0 20px 20px;text-align:center;color:var(--white);padding-top:10px}
.card-heading{font-family:'Roboto Condensed',sans-serif;font-weight:700;font-size:18px;color:var(--white)}
.donate-note{font-family:'Roboto Condensed',sans-serif;font-weight:700;font-size:12.5px;color:#2a3a10;margin:14px 8px 0;line-height:15px}
.pay-button{display:inline-block;margin-top:24px;width:76px;height:46px;border-radius:6px;background:linear-gradient(180deg,#fff,#f1e6c9);border:1px solid #d4b57a;color:#1d3f86;font-weight:bold;font-size:15px;line-height:44px}
.sponsor{left:201px;top:757px;width:527px;height:156px}
.sponsor-inner{height:100%;background:var(--green);display:flex}
.sponsor-text{width:230px;padding:8px 10px}
.sponsor-address{font-family:Georgia,'Gelasio',serif;font-size:12.3px;line-height:19px;color:var(--white);margin-top:12px;word-break:break-all}
.sponsor-address .muted{color:#d9ecb0}
.sponsor-photo{flex:1;background:linear-gradient(160deg,#d7cdb6,#a89a82 50%,#e6e6e6)}
.newsletter{left:29px;top:943px;width:163px;height:170px;border-radius:0 0 50% 50%/0 0 22px 22px}
.newsletter-inner{height:100%;background:var(--orange);border-radius:0 0 50% 50%/0 0 20px 20px;padding:5px 6px 0}
.news-kicker{font-family:'Roboto Condensed',sans-serif;font-weight:700;font-size:11.5px;color:var(--white)}
.news-title{font-family:'Roboto Condensed',sans-serif;font-weight:700;font-size:17px;color:#111;line-height:17px}
.news-note{font-size:9px;line-height:13px;margin:4px 0 6px}
.field{display:block;width:100%;height:20px;background:var(--white);border:1px solid #ccc;font-size:8.5px;color:#888;padding:4px 5px;margin-bottom:6px}
.submit{display:block;margin:6px auto 0;width:78px;height:20px;background:linear-gradient(180deg,#9ad42a,var(--green-dark));border:1px solid #5e8a10;font-family:Georgia,serif;font-size:12px;text-align:center;line-height:18px}
.story{left:201px;top:943px;width:527px;height:157px}
.story-inner{height:100%;background:var(--green);display:flex;padding:8px 12px 8px 8px;gap:20px}
.story-text{width:290px}
.story-body{font-size:10.5px;line-height:15px;color:var(--white);margin-top:6px;height:90px;overflow:hidden}
.story-more{color:var(--white);font-size:10px;text-decoration:underline;display:inline-block;margin-top:6px}
.story-photo{flex:1;margin-top:6px;height:126px;background:linear-gradient(180deg,#e9e7da 0%,#c9c2b2 30%,#9b8d7a 60%,var(--photo-crowd))}
.footer{left:0;top:1130px;width:765px;height:70px;background:var(--footer);color:var(--white);font-size:10.5px}
.footer-col{position:absolute;top:10px}
.footer-col h4{font-weight:normal;font-size:10.5px;margin-bottom:10px}
.footer-col p{font-size:9px;line-height:12px}
.accent{color:var(--orange)}
.follow{display:flex;gap:5px}
.follow span{width:22px;height:22px;border-radius:50%;background:#f2f2f2}
</style>
</head>
<body>
<header class="abs header"></header>
<div class="abs brand"><span class="brand-name">Youngsters Unite</span><span class="brand-dot"></span></div>
<div class="abs social-badge">FIND US ON PLIXA</div>

<nav class="abs nav">
  <a href="#">Home</a><a href="#">Donate</a><a href="#">Become a Sponsor</a><a href="#">History</a><a href="#">News</a><a href="#">Contact Us</a>
</nav>

<section class="abs slider">
  <div class="slide-photo" role="img" aria-label="Teen volunteers collecting donations at a crowded fundraising tent">
    <div class="slide-caption">Helping Others Around The World</div>
  </div>
</section>
<div class="abs arrow arrow-left"><svg width="33" height="37" viewBox="0 0 33 37"><path d="M21 10 L11 18.5 L21 27 Z" fill="#fff"/></svg></div>
<div class="abs arrow arrow-right"><svg width="33" height="37" viewBox="0 0 33 37"><path d="M12 10 L22 18.5 L12 27 Z" fill="#fff"/></svg></div>

<h2 class="abs mission-title">Our Mission</h2>
<p class="abs mission-text">Support each other, the environment and the poor, through fund raising and other philanthropic efforts.</p>
<a class="abs read-more mission-more" href="#">Read more</a>
<div class="abs mission-photo"><div role="img" aria-label="Young founder standing in a coastal marsh"></div></div>

<div class="abs causes">
  <span class="cause"><svg viewBox="0 0 20 20"><circle cx="10" cy="10" r="8.5" fill="none" stroke="#f39a1e" stroke-width="2"/><path d="M6 10h7M10 6.5l3.5 3.5-3.5 3.5" fill="none" stroke="#f39a1e" stroke-width="2"/></svg>Hunger</span>
  <span class="cause"><svg viewBox="0 0 20 20"><circle cx="10" cy="10" r="8.5" fill="none" stroke="#f39a1e" stroke-width="2"/><path d="M6 10h7M10 6.5l3.5 3.5-3.5 3.5" fill="none" stroke="#f39a1e" stroke-width="2"/></svg>Disaster Relief</span>
  <span class="cause"><svg viewBox="0 0 20 20"><circle cx="10" cy="10" r="8.5" fill="none" stroke="#f39a1e" stroke-width="2"/><path d="M6 10h7M10 6.5l3.5 3.5-3.5 3.5" fill="none" stroke="#f39a1e" stroke-width="2"/></svg>Water</span>
  <span class="cause"><svg viewBox="0 0 20 20"><circle cx="10" cy="10" r="8.5" fill="none" stroke="#f39a1e" stroke-width="2"/><path d="M6 10h7M10 6.5l3.5 3.5-3.5 3.5" fill="none" stroke="#f39a1e" stroke-width="2"/></svg>Medical</span>
  <span class="cause"><svg viewBox="0 0 20 20"><circle cx="10" cy="10" r="8.5" fill="none" stroke="#f39a1e" stroke-width="2"/><path d="M6 10h7M10 6.5l3.5 3.5-3.5 3.5" fill="none" stroke="#f39a1e" stroke-width="2"/></svg>Environment</span>
</div>

<section class="abs card donate">
  <div class="donate-inner">
    <h3 class="card-heading">DONATE US</h3>
    <p class="donate-note">100% of Donations Go To Causes</p>
    <span class="pay-button">Coinvo</span>
  </div>
</section>

<section class="abs card sponsor">
  <div class="sponsor-inner">
    <div class="sponsor-text">
      <h3 class="card-heading">BECOME A SPONSOR</h3>
      <p class="sponsor-address"><span class="muted">YOUNGSTERS UNITE CORP.</span><br>418 HARBOR LANE<br>COVE POINT, NJ 08099<br>CUSTOMERSERVICE@YOUNGSTERSUNITE.ORG</p>
    </div>
    <div class="sponsor-photo" role="img" aria-label="Three people holding a large donation check"></div>
  </div>
</section>

<section class="abs card newsletter">
  <div class="newsletter-inner">
    <div class="news-kicker">Subscribe</div>
    <div class="news-title">NEWSLETTER</div>
    <p class="news-note">To get all latest news about our work subscribe</p>
    <span class="field">Type your name</span>
    <span class="field">Type your email id</span>
    <span class="submit">Submit</span>
  </div>
</section>

<section class="abs card story">
  <div class="story-inner">
    <div class="story-text">
      <h3 class="card-heading">HOW IT ALL GOT STARTED</h3>
      <p class="story-body">During the summer of 2010, a group of teens from Cove Point, NJ wanted to do something to help with the disaster in the Gulf. They raised thousands of dollars and 100% of the money was donated to help save animals. Sponsors funded the administration costs. It was a huge success and</p>
      <a class="story-more" href="#">Read More</a>
    </div>
    <div class="story-photo" role="img" aria-label="Group of teen volunteers in matching shirts in front of a banner"></div>
  </div>
</section>

<footer class="abs footer">
  <div class="footer-col" style="left:16px">
    <h4>Contact Us:</h4>
    <p>Mail id: : <span class="accent">customerservice@youngstersunite.org</span><br>Phone: <span class="accent">555-217-4630</span></p>
  </div>
  <div class="footer-col" style="left:325px">
    <h4>Follow Us:</h4>
    <div class="follow"><span aria-label="Plixa"></span><span aria-label="Chirpa"></span><span aria-label="Workly"></span></div>
  </div>
  <div class="footer-col" style="left:575px">
    <h4>Copyright</h4>
    <p class="accent">Youngstersunite<br>©2012, All Rights Reserved</p>
  </div>
</footer>
</body>
</html>
```